1. Create Christmas and Happy New Year concept / concepts proposal, optionally using the artworks attached;
2. Based on the concepts please elaborate necessary formats for the following communication channels:
- DEM email to our customers;
- Social media posts (FB, IG and LKND)
- Banner placed under the company signature (size 72 dpi).
The winner is kindly asked to upload the files in open format in Adobe InDesign or Adobe Illustrator.
Logo: “must have” in social media posts.
Colors to be used: red (pantone 1795 C ) , shades of gray and or silver.

Target Market(s)

Professional world b2b

Font styles to use
Other font styles liked:
• Helvetica styles

Colors
EB3D1F
EC4F4E
F09395
F8D3D4
FCEDEE

Requirements
Must have
• Elegant design is preferred with harmonious colour palette.

```html
<!DOCTYPE html>
<html lang="en">
<head>
<meta charset="utf-8">
<title>Christmas &amp; New Year Campaign – Valtor</title>
<link href="https://fonts.googleapis.com/css2?family=Cinzel:wght@400;600;700&family=Great+Vibes&family=Montserrat:wght@300;400;500;600;700&family=Poppins:wght@500&display=swap" rel="stylesheet">
<style>
:root{
  --red:#e8221d;
  --red-deep:#c4120f;
  --red-soft:#ec4f4e;
  --pink:#f09395;
  --pink-pale:#f8d3d4;
  --blush:#fcedee;
  --canvas:#ebebeb;
  --grey-dark:#4a4a4a;
  --grey:#8a8a8a;
  --grey-light:#bdbdbd;
  --silver:#e4e4e4;
  --white:#ffffff;
  --btn-blue:#4267b2;
  --btn-steel:#2a6fa8;
}
*{box-sizing:border-box;margin:0;padding:0}
html,body{width:1200px;height:2400px;overflow:hidden;background:var(--canvas)}
.board{position:relative;width:1200px;height:2400px;background:var(--canvas);font-family:'Montserrat',Helvetica,Arial,sans-serif}
.piece{position:absolute;overflow:hidden;box-shadow:0 4px 10px rgba(0,0,0,.18)}
.abs{position:absolute}
.label{position:absolute;font-family:'Poppins',Helvetica,Arial,sans-serif;font-weight:500;font-size:32px;color:#2a2a2a;letter-spacing:.5px;white-space:nowrap}

.red-scene{position:absolute;left:0;top:0;width:100%;
  background:radial-gradient(ellipse at 50% 45%,var(--red-soft) 0%,var(--red) 45%,var(--red-deep) 100%)}
.ornaments{position:absolute;left:0;top:0;width:100%;
  background:linear-gradient(180deg,rgba(248,211,212,.45),rgba(240,147,149,.2) 70%,rgba(240,147,149,0));}
.village{position:absolute;left:0;width:100%}
.village svg{display:block;width:100%;height:100%}
.serif{font-family:'Cinzel',Georgia,serif;font-weight:700;color:var(--white);text-align:center;position:absolute;left:0;width:100%;line-height:1;white-space:nowrap}
.script{font-family:'Great Vibes',cursive;color:var(--white);text-align:center;position:absolute;left:0;width:100%;line-height:1;white-space:nowrap}
.spaced{font-family:'Cinzel',Georgia,serif;font-weight:700;color:var(--white);text-align:center;position:absolute;left:0;width:100%;line-height:1;white-space:nowrap}

.bristles{position:absolute;left:0;width:100%;
  background:radial-gradient(ellipse at 50% 50%,#fafafa 0%,#e9e9e9 60%,#dcdcdc 100%)}

.sale-kicker{position:absolute;color:var(--grey);font-weight:400;letter-spacing:.22em;text-align:center;white-space:nowrap}
.sale-line{position:absolute;height:2px;background:var(--red)}
.sale-rule{position:absolute;height:1px;background:var(--grey-light)}
.sale-save{position:absolute;font-family:'Cinzel',Georgia,serif;color:var(--red);font-weight:600;line-height:1;white-space:nowrap;display:flex;align-items:center;justify-content:center}
.sale-save .upto{font-family:'Montserrat',sans-serif;color:var(--grey);font-weight:400;line-height:.9;display:inline-flex;flex-direction:column;margin:0 .12em}
.sale-save sup{font-size:.5em;vertical-align:top}
.sale-sub{position:absolute;color:var(--grey-dark);font-weight:600;text-align:center;white-space:nowrap}
.site-bar{position:absolute;background:#6d6d6d;color:var(--white);text-align:center;font-weight:600;letter-spacing:.35em;white-space:nowrap}

.tile{position:absolute;background:var(--red)}
.tile .product{position:absolute;inset:10% 14%;border-radius:50%;
  background:radial-gradient(circle at 40% 40%,#cfcfcf 0%,#7b7b7b 55%,#333 100%)}

.dem{left:143px;top:96px;width:416px;height:1284px;background:var(--silver)}
.brand-mark{position:absolute;display:flex;align-items:center;gap:8px;color:var(--white);font-weight:700;font-size:26px;letter-spacing:.06em}
.brand-mark .sq{width:22px;height:22px;background:var(--white)}
.shop-btn{position:absolute;left:154px;top:1013px;width:108px;height:27px;background:var(--grey);color:var(--white);border-radius:3px;font-weight:700;font-size:15px;text-align:center;line-height:27px}
.dem-foot{position:absolute;left:0;width:100%;text-align:center;color:#a3a3a3;font-size:10.5px;line-height:13px}
.dem-foot .hl{color:var(--red);font-weight:600}
.soc-dot{display:inline-block;width:14px;height:14px;background:#a8a8a8;border-radius:2px;margin:0 3px}

.fb{left:637px;top:96px;width:418px;height:418px;background:var(--white)}
.ig{left:637px;top:628px;width:418px;height:218px}
.lk{left:637px;top:947px;width:418px;height:219px;background:var(--white)}

.banner{left:147px;top:1510px;width:907px;height:731px;background:var(--white);border-top:3px solid var(--red)}
.ft{position:absolute;font-size:9.5px;color:#777;line-height:14px}
.ft-head{position:absolute;font-size:9.5px;font-weight:600;color:#444;letter-spacing:.03em}
.ft-link{position:absolute;left:298px;width:147px;font-size:8.5px;color:#777;border-bottom:1px solid #e6e6e6;padding-bottom:5px}
.ft-red{color:var(--red)}
.btn-mini{position:absolute;height:13px;font-size:7.5px;font-weight:700;color:var(--white);line-height:13px;padding:0 6px;border-radius:2px}
.newsletter-in{position:absolute;left:621px;top:133px;width:154px;height:19px;border:1px solid #ccc;font-size:8px;color:#999;line-height:17px;padding-left:10px}
.newsletter-in span{position:absolute;right:0;top:0;height:17px;width:58px;border-left:1px solid #ccc;color:#333;text-align:center;background:#f6f6f6}
</style>
</head>
<body>
<div class="board">

  <section class="piece dem" aria-label="Christmas email">
    <div class="red-scene" style="height:475px" role="img" aria-label="Red-toned brush factory production line in the background"></div>
    <div class="ornaments" style="height:150px;left:0;width:120px" role="img" aria-label="Hanging ornaments: snowmen, Santa figures and glasses"></div>
    <div class="ornaments" style="height:150px;left:296px;width:120px" role="img" aria-label="Hanging ornaments: snowmen, Santa figures and glasses"></div>
    <div class="brand-mark" style="left:132px;top:82px"><span class="sq"></span>VALTOR</div>
    <div class="serif" style="top:190px;font-size:40px">MERRY</div>
    <div class="serif" style="top:226px;font-size:52px">CHRISTMAS</div>
    <div class="serif" style="top:276px;font-size:28px;font-weight:400">&amp;</div>
    <div class="serif" style="top:310px;font-size:38px">HAPPY</div>
    <div class="serif" style="top:348px;font-size:38px">NEW YEAR</div>
    <div class="bristles" style="top:475px;height:809px" role="img" aria-label="Soft white brush bristles texture"></div>
    <div class="village" style="top:430px;height:50px" role="img" aria-label="Snowy village silhouette with houses, trees and reindeer">
      <svg viewBox="0 0 416 50" preserveAspectRatio="none"><path d="M0 30 Q52 18 104 30 T208 28 T312 30 T416 24 V50 H0Z" fill="#ffffff" opacity=".95"/></svg>
    </div>

    <div class="sale-kicker" style="left:0;width:416px;top:515px;font-size:20px">YEAR ENDING SALE</div>
    <div class="sale-line" style="left:70px;top:545px;width:277px"></div>
    <div class="sale-save" style="left:0;width:416px;top:553px;font-size:52px">SAVE<span class="upto" style="font-size:14px"><span>UP</span><span>TO</span></span>30<sup>%</sup></div>
    <div class="sale-sub" style="left:0;width:416px;top:600px;font-size:9.5px">Technical Brushes &amp; Special Applications for the Industry</div>
    <div class="sale-rule" style="left:70px;top:615px;width:277px"></div>

    <div class="tile" style="left:151px;top:658px;width:115px;height:76px"><div class="product" role="img" aria-label="Cylindrical wire brush"></div></div>
    <div class="tile" style="left:89px;top:741px;width:115px;height:76px"><div class="product" role="img" aria-label="Knotted wire wheel brushes"></div></div>
    <div class="tile" style="left:207px;top:741px;width:120px;height:76px"><div class="product" role="img" aria-label="Strip brushes with yellow and black bristles"></div></div>
    <div class="tile" style="left:30px;top:825px;width:115px;height:76px"><div class="product" role="img" aria-label="Twisted wire wheel brushes"></div></div>
    <div class="tile" style="left:151px;top:825px;width:115px;height:76px"><div class="product" role="img" aria-label="Green cup brush"></div></div>
    <div class="tile" style="left:271px;top:825px;width:115px;height:76px"><div class="product" role="img" aria-label="Crimped wire wheel brush"></div></div>
    <div class="tile" style="left:89px;top:909px;width:115px;height:76px"><div class="product" role="img" aria-label="Wheel brush with hex hub"></div></div>
    <div class="tile" style="left:207px;top:909px;width:120px;height:76px"><div class="product" role="img" aria-label="Abrasive roller brush"></div></div>

    <div class="shop-btn">SHOP NOW</div>
    <div class="dem-foot" style="top:1066px">If you have any questions,<br>please email us at <b>info@valtorbrush.com</b> or visit our FAQs .</div>
    <div class="dem-foot" style="top:1106px"><span class="soc-dot"></span><span class="soc-dot"></span></div>
    <div class="dem-foot" style="top:1142px">Brushes for Grinders | Brushes for Drills | FAQ | Technical Information<br>| Security Information</div>
    <div class="dem-foot" style="top:1181px">Via dei Tigli 18 Zola Predosa 40069 Bologna, Italy.<br>Company Number: <span class="hl">+39 051 4820376</span><br><span class="hl">info@valtorbrush.com</span></div>
  </section>
  <div class="label" style="left:262px;top:1406px">DEM EMAIL</div>

  <section class="piece fb" aria-label="Facebook post">
    <div class="red-scene" style="height:250px" role="img" aria-label="Red-toned factory background"></div>
    <div class="ornaments" style="height:55px" role="img" aria-label="Row of Christmas ornaments: bells, stars, snowflakes, candy canes"></div>
    <div class="serif" style="top:52px;font-size:44px">MERRY</div>
    <div class="serif" style="top:86px;font-size:54px">CHRISTMAS</div>
    <div class="serif" style="top:136px;font-size:26px;font-weight:400">&amp;</div>
    <div class="serif" style="top:166px;font-size:32px">HAPPY NEW YEAR</div>
    <div class="bristles" style="top:250px;height:168px" role="img" aria-label="White brush bristles texture"></div>
    <div class="village" style="top:212px;height:44px" role="img" aria-label="Snowy village silhouette">
      <svg viewBox="0 0 418 44" preserveAspectRatio="none"><path d="M0 26 Q70 14 140 26 T280 24 T418 22 V44 H0Z" fill="#ffffff"/></svg>
    </div>
    <div class="sale-kicker" style="left:22px;width:190px;top:279px;font-size:14px">YEAR ENDING SALE</div>
    <div class="sale-line" style="left:22px;top:299px;width:187px"></div>
    <div class="sale-save" style="left:12px;width:210px;top:302px;font-size:40px">SAVE<span class="upto" style="font-size:11px"><span>UP</span><span>TO</span></span>30<sup>%</sup></div>
    <div class="sale-sub" style="left:12px;width:210px;top:339px;font-size:6.5px">Technical Brushes &amp; Special Applications for the Industry</div>
    <div class="sale-rule" style="left:22px;top:350px;width:187px"></div>
    <div class="site-bar" style="left:24px;top:371px;width:184px;height:15px;font-size:10px;line-height:15px">www.valtorbrush.com</div>
    <div class="tile" style="left:296px;top:256px;width:49px;height:30px"><div class="product" role="img" aria-label="Cylindrical brush"></div></div>
    <div class="tile" style="left:272px;top:290px;width:48px;height:33px"><div class="product" role="img" aria-label="Knotted wheel brush"></div></div>
    <div class="tile" style="left:322px;top:290px;width:49px;height:33px"><div class="product" role="img" aria-label="Strip brush"></div></div>
    <div class="tile" style="left:246px;top:326px;width:47px;height:32px"><div class="product" role="img" aria-label="Wire wheels"></div></div>
    <div class="tile" style="left:296px;top:326px;width:49px;height:32px"><div class="product" role="img" aria-label="Cup brush"></div></div>
    <div class="tile" style="left:347px;top:326px;width:48px;height:32px"><div class="product" role="img" aria-label="Wire wheel"></div></div>
    <div class="tile" style="left:272px;top:363px;width:48px;height:31px"><div class="product" role="img" aria-label="Hub wheel brush"></div></div>
    <div class="tile" style="left:322px;top:363px;width:49px;height:31px"><div class="product" role="img" aria-label="Roller brush"></div></div>
  </section>
  <div class="label" style="left:637px;top:542px">FB SOCIAL MEDIA POST</div>

  <section class="piece ig" aria-label="Instagram post">
    <div class="red-scene" style="height:218px" role="img" aria-label="Red-toned factory background"></div>
    <div class="ornaments" style="height:50px" role="img" aria-label="Row of hanging Christmas ornaments"></div>
    <div class="script" style="top:64px;font-size:58px">Merry Christmas</div>
    <div class="serif" style="top:120px;font-size:20px;font-weight:400">&amp;</div>
    <div class="spaced" style="top:145px;font-size:24px;letter-spacing:6px">HAPPY NEW YEAR</div>
    <div class="village" style="top:186px;height:32px" role="img" aria-label="Snowy village silhouette">
      <svg viewBox="0 0 418 32" preserveAspectRatio="none"><path d="M0 18 Q70 8 140 18 T280 16 T418 14 V32 H0Z" fill="#ffffff"/></svg>
    </div>
  </section>
  <div class="label" style="left:637px;top:872px">IG SOCIAL MEDIA POST</div>

  <section class="piece lk" aria-label="LinkedIn post">
    <div class="red-scene" style="height:146px" role="img" aria-label="Red-toned factory background"></div>
    <div class="ornaments" style="height:45px" role="img" aria-label="Row of hanging Christmas ornaments"></div>
    <div class="serif" style="top:55px;font-size:32px">MERRY CHRISTMAS</div>
    <div class="serif" style="top:86px;font-size:19px">&amp; HAPPY NEW YEAR</div>
    <div class="bristles" style="top:146px;height:73px" role="img" aria-label="White brush bristles texture"></div>
    <div class="village" style="top:116px;height:34px" role="img" aria-label="Snowy village silhouette">
      <svg viewBox="0 0 418 34" preserveAspectRatio="none"><path d="M0 22 Q70 12 140 22 T280 20 T418 18 V34 H0Z" fill="#ffffff"/></svg>
    </div>
    <div class="tile" style="left:38px;top:147px;width:30px;height:28px;background:none"><div class="product" style="inset:0" role="img" aria-label="Cylindrical brush"></div></div>
    <div class="tile" style="left:12px;top:176px;width:35px;height:28px"><div class="product" role="img" aria-label="Knotted wheel brush"></div></div>
    <div class="tile" style="left:50px;top:176px;width:35px;height:28px"><div class="product" role="img" aria-label="Roller brush"></div></div>
    <div class="sale-kicker" style="left:144px;width:140px;top:151px;font-size:10px">YEAR ENDING SALE</div>
    <div class="sale-line" style="left:144px;top:164px;width:136px;height:1px"></div>
    <div class="sale-save" style="left:134px;width:156px;top:165px;font-size:28px">SAVE<span class="upto" style="font-size:8px"><span>UP</span><span>TO</span></span>30<sup>%</sup></div>
    <div class="sale-sub" style="left:134px;width:156px;top:191px;font-size:4.6px">Technical Brushes &amp; Special Applications for the Industry</div>
    <div class="site-bar" style="left:164px;top:200px;width:96px;height:7px;font-size:5px;line-height:7px">www.valtorbrush.com</div>
    <div class="tile" style="left:315px;top:150px;width:36px;height:28px;background:none"><div class="product" style="inset:0" role="img" aria-label="Wire wheels"></div></div>
    <div class="tile" style="left:354px;top:150px;width:36px;height:28px"><div class="product" role="img" aria-label="Cup brush"></div></div>
    <div class="tile" style="left:345px;top:180px;width:44px;height:36px;background:none"><div class="product" style="inset:0" role="img" aria-label="Wire wheel"></div></div>
  </section>
  <div class="label" style="left:637px;top:1194px">LKND SOCIAL MEDIA POST</div>

  <section class="piece banner" aria-label="Email signature banner with website footer">
    <div class="abs" style="left:137px;top:44px;display:flex;align-items:flex-start;gap:6px">
      <span style="width:36px;height:36px;background:var(--red);flex:none"></span>
      <span style="color:var(--red);font-weight:600;font-size:13px;line-height:14px">Valtor<br>Spazzole<br>Industriali</span>
    </div>
    <div class="ft" style="left:137px;top:94px">Via dei Tigli 18<br>Zola Predosa<br>40069 Bologna, Italy.</div>
    <div class="ft ft-red" style="left:137px;top:145px;font-size:8.5px;line-height:13px">+39 051 4820376<br>info@valtorbrush.com<br>VCard</div>
    <div class="abs" style="left:137px;top:198px;display:flex;gap:6px">
      <span style="width:14px;height:14px;border-radius:50%;background:#b0b0b0"></span>
      <span style="width:14px;height:14px;border-radius:2px;background:#b0b0b0"></span>
    </div>

    <div class="ft-head" style="left:298px;top:38px">USEFUL PAGES</div>
    <div class="sale-rule" style="left:298px;top:70px;width:147px;background:#e6e6e6"></div>
    <div class="ft-link" style="top:81px">Brushes for Grinders</div>
    <div class="ft-link" style="top:106px">Brushes for Drills</div>
    <div class="ft-link" style="top:130px">FAQ</div>
    <div class="ft-link" style="top:155px">Technical Information</div>
    <div class="ft-link" style="top:180px;border:none">Security Information</div>

    <div class="ft-head" style="left:459px;top:38px">WIRE BRUSHES ARE SOCIAL!</div>
    <div class="sale-rule" style="left:459px;top:70px;width:147px;background:#e6e6e6"></div>
    <div class="ft" style="left:459px;top:81px;font-size:7.5px;color:#999">stay updated</div>
    <div class="btn-mini" style="left:463px;top:116px;background:var(--btn-blue)">Segui</div>
    <div class="btn-mini" style="left:514px;top:116px;background:var(--btn-blue)">Condividi</div>
    <div class="btn-mini" style="left:459px;top:149px;background:var(--btn-steel);padding:0 8px">Follow</div>
    <div class="ft" style="left:520px;top:149px;font-size:7.5px;line-height:13px;border:1px solid #ccc;padding:0 3px">2,580</div>
    <div class="btn-mini" style="left:459px;top:165px;background:var(--red)">Watch</div>

    <div class="ft-head" style="left:621px;top:38px">NEWSLETTER</div>
    <div class="ft" style="left:621px;top:72px;font-size:9px;line-height:13px">Subscribe to our newsletter to<br>stay up to date and receive offers<br>and promotions</div>
    <div class="newsletter-in">Newsletter..<span>Subscribe</span></div>
    <div class="ft" style="left:621px;top:173px;font-size:7.5px;display:flex;align-items:center;gap:3px"><span style="width:8px;height:8px;border:1px solid #888"></span>I accept the <span class="ft-red">privacy policy</span></div>
    <div class="ft" style="left:621px;top:200px;font-size:7px;line-height:13px;color:#999">Don't worry! Your data is safe with us! For<br>further information read our <span class="ft-red">privacy policy</span></div>

    <div class="red-scene" style="top:276px;height:452px" role="img" aria-label="Red-toned factory background"></div>
    <div class="ornaments" style="top:276px;height:135px" role="img" aria-label="Row of hanging Christmas ornaments: bells, angels, stars, gifts, candy canes"></div>
    <div class="script" style="top:420px;font-size:112px">Merry Christmas</div>
    <div class="serif" style="top:525px;font-size:44px;font-weight:400">&amp;</div>
    <div class="spaced" style="top:575px;font-size:52px;letter-spacing:12px">HAPPY NEW YEAR</div>
    <div class="village" style="top:672px;height:56px" role="img" aria-label="Snowy village silhouette with houses, trees and reindeer">
      <svg viewBox="0 0 907 56" preserveAspectRatio="none"><path d="M0 34 Q150 18 300 34 T600 30 T907 28 V56 H0Z" fill="#ffffff"/></svg>
    </div>
  </section>
  <div class="label" style="left:346px;top:2275px">BANNER COMPANY SIGNATURE</div>

</div>
</body>
</html>
```